I would like a minimalist clean and uncluttered website design.
Initially, I would like to see a front page only and would then like to build on the project front there.
RTV logo file with no background is attached, can be grey scale if the designer wishes.
I would like the front page to speak about the company's ethos and goals and I will need to put a great deal of thought into this to ensure it has the desired impact with the content on the subsequent pages.
The paragraph below gives a bit of an idea as to what this will include.
"RTV is a technology company providing approachable IT products and services to business:
With the overwhelming advancements in technology, businesses often find it difficult to determine what is available and what best suits their businesses specific needs.
We can assist business with their IT infrustucture, devices, software in procurement, installation, training, cost control as well as ongoing administration and support. We also keep our Clients informed of new technology and products which can benefit them"
Target Market(s)
Business, Health, Education, Professional Practices. Target age would be around 30 plus either male or female. Office administration level through Managing Directors. English speaking.

```html
<!DOCTYPE html>
<html lang="en">
<head>
<meta charset="utf-8">
<title>RTV – Approachable IT for Business</title>
<link href="https://fonts.googleapis.com/css2?family=Open+Sans:ital,wght@0,400;0,600;0,700;1,400&display=swap" rel="stylesheet">
<style>
:root{
  --blue:#1f6db3;
  --blue-dark:#17599a;
  --blue-light:#3d8bd0;
  --text:#444;
  --muted:#8a8a8a;
  --line:#e3e3e3;
  --soft:#f2f2f2;
  --band:#6a6a6a;
  --footer:#3b3b3b;
  --footer-deep:#2c2c2c;
  --white:#fff;
}
*{box-sizing:border-box;margin:0;padding:0}
html,body{width:779px;height:1200px;overflow:hidden}
body{font-family:"Open Sans",Arial,sans-serif;color:var(--text);background:var(--white);position:relative;font-size:10px}
.top-rule{height:4px;background:var(--blue)}
.settings-tab{position:absolute;left:0;top:62px;width:15px;height:108px;background:var(--blue);color:var(--white);font-size:7px;writing-mode:vertical-rl;display:flex;align-items:center;justify-content:center;letter-spacing:.5px}
.header{position:relative;height:95px}
.brand{position:absolute;left:44px;top:18px;display:flex;align-items:center;gap:8px}
.brand-mark{width:22px;height:22px;background:var(--blue)}
.brand-name{font-size:34px;font-weight:700;color:var(--blue);letter-spacing:2px}
.header-right{position:absolute;right:24px;top:20px;text-align:right}
.social{display:flex;gap:8px;justify-content:flex-end;margin-bottom:6px}
.social span{width:9px;height:9px;border-radius:50%;background:#b5b5b5}
.contact{font-size:9px;color:#666}
.contact strong{color:var(--blue)}
.nav{position:absolute;left:22px;top:99px;width:737px;height:26px;background:var(--blue);display:flex;align-items:center}
.nav a{color:var(--white);text-decoration:none;font-size:8.5px;font-weight:600;padding:0 13px;height:26px;line-height:26px}
.nav a.active{background:var(--blue-light)}
.search{position:absolute;right:6px;top:5px;width:125px;height:16px;background:var(--white);font-size:8px;color:#999;padding:2px 6px}
.hero{position:absolute;left:22px;top:125px;width:737px;height:320px}
.hero-logo{position:absolute;left:22px;top:40px;display:flex;align-items:center;gap:14px}
.hero-logo .brand-mark{width:44px;height:44px}
.hero-logo .brand-name{font-size:70px;letter-spacing:4px}
.hero-quote{position:absolute;left:18px;top:182px;width:212px;background:var(--blue);color:var(--white);font-weight:700;font-size:11px;line-height:1.45;padding:9px 12px}
.hero-photo{position:absolute;left:348px;top:8px;width:350px;height:310px;background:radial-gradient(ellipse at 50% 45%,#dde3ea 0%,#f4f6f8 70%,#fff 100%)}
.band{position:absolute;left:0;top:450px;width:779px;height:50px;background:var(--band);color:var(--white);font-style:italic;font-size:16px;display:flex;align-items:center;padding-left:22px}
.features{position:absolute;left:40px;top:512px;width:700px;display:flex;justify-content:space-between}
.feature{width:205px}
.feature h3{font-size:12px;font-weight:600;display:flex;align-items:center;gap:8px;margin-bottom:8px}
.icon{width:16px;height:16px;border-radius:50%;border:1.5px solid var(--blue)}
.feature p{font-size:8px;line-height:1.55;color:var(--muted);padding-left:24px;margin-bottom:10px}
.btn{display:inline-block;background:var(--blue);color:var(--white);font-size:8px;padding:4px 10px}
.feature .btn{margin-left:24px}
.projects{position:absolute;left:0;top:640px;width:779px;height:195px;background:var(--soft)}
.projects-intro{position:absolute;left:40px;top:18px;width:170px}
.projects-intro h3{font-size:12px;font-weight:600;margin-bottom:10px}
.projects-intro p{font-size:8px;line-height:1.55;color:var(--muted);margin-bottom:12px}
.cards{position:absolute;left:225px;top:14px;display:flex;gap:12px}
.card{width:170px;background:var(--white)}
.card-img{height:92px}
.card-img.a{background:linear-gradient(135deg,#9cc3e6,#d9e8f5)}
.card-img.b{background:linear-gradient(135deg,#c9d6e3,#eef2f6)}
.card-img.c{background:linear-gradient(135deg,#b7a99a,#e9e1d8)}
.card-body{text-align:center;padding:7px 4px 8px}
.card-body h4{font-size:9px;font-weight:400;color:#555}
.card-body span{font-size:7px;color:var(--muted)}
.arrows{position:absolute;right:30px;top:172px;display:flex;gap:3px}
.arrows span{width:11px;height:11px;background:#999}
.arrows span:last-child{background:var(--blue)}
.partners{position:absolute;left:40px;top:855px;width:700px;height:85px;display:flex;justify-content:space-between;align-items:center}
.badge{width:118px;height:40px;background:#d8d8d8;border-radius:4px}
.footer{position:absolute;left:0;top:955px;width:779px;height:210px;background:var(--footer);color:#bbb}
.fcol{position:absolute;top:22px}
.fcol h4{font-size:9px;color:var(--white);font-weight:600;letter-spacing:.5px;margin-bottom:12px}
.fcol .title{font-size:17px;font-weight:700;color:var(--white);letter-spacing:0;margin-bottom:2px}
.fcol .sub{font-size:7px;color:var(--muted);margin-bottom:10px}
.fcol p{font-size:7.5px;line-height:1.6;margin-bottom:8px}
.fcol ul{list-style:none;font-size:7.5px}
.fcol li{margin-bottom:10px}
.photos{display:grid;grid-template-columns:repeat(3,32px);gap:8px}
.photos span{height:26px;background:linear-gradient(135deg,#6d6f78,#9a8f84)}
.bottom-bar{position:absolute;left:0;top:1165px;width:779px;height:35px;background:var(--footer-deep);color:#999;font-size:7.5px;padding:12px 40px}
</style>
</head>
<body>
<div class="top-rule"></div>
<div class="settings-tab">Theme Settings</div>

<header class="header">
  <div class="brand"><span class="brand-mark"></span><span class="brand-name">RTV</span></div>
  <div class="header-right">
    <div class="social"><span></span><span></span><span></span><span></span><span></span><span></span></div>
    <div class="contact">CONTACT PHONE: <strong>+000 000 0000 000</strong></div>
  </div>
</header>

<nav class="nav">
  <a class="active">HOME</a><a>PAGES</a><a>PORTFOLIO</a><a>BLOG</a><a>SHORTCODES</a><a>CONTACT US</a>
  <div class="search">Search</div>
</nav>

<section class="hero">
  <div class="hero-logo"><span class="brand-mark"></span><span class="brand-name">RTV</span></div>
  <div class="hero-quote">"RTV Is A Technology Company Providing Approachable IT Products And Services To Business."</div>
  <div class="hero-photo" role="img" aria-label="Photo of two smiling business professionals in suits"></div>
</section>

<div class="band">"We are Different From Others Because We Believe in Satisfaction."</div>

<section class="features">
  <div class="feature">
    <h3><span class="icon"></span>About Us</h3>
    <p>We guide businesses through technology choices and deliver practical IT that suits their needs.</p>
    <span class="btn">See More</span>
  </div>
  <div class="feature">
    <h3><span class="icon"></span>Our Services</h3>
    <p>Procurement, installation, training and cost control, plus ongoing administration and support for your team.</p>
    <span class="btn">See More</span>
  </div>
  <div class="feature">
    <h3><span class="icon"></span>Our Products</h3>
    <p>Devices, software and infrastructure chosen carefully, and news on technology that benefits our clients.</p>
    <span class="btn">See More</span>
  </div>
</section>

<section class="projects">
  <div class="projects-intro">
    <h3>Our Recent Projects</h3>
    <p>Recent work for clients across health, education and professional practice sectors.</p>
    <span class="btn">Our Portfolio</span>
  </div>
  <div class="cards">
    <div class="card"><div class="card-img a" role="img" aria-label="Screens showing a website theme"></div><div class="card-body"><h4>Custom Website Theme</h4><span>Web / Development</span></div></div>
    <div class="card"><div class="card-img b" role="img" aria-label="Hands at a laptop keyboard"></div><div class="card-body"><h4>T-Shirt Design</h4><span>Print / Branding</span></div></div>
    <div class="card"><div class="card-img c" role="img" aria-label="Team of professionals posing together"></div><div class="card-body"><h4>Video Project</h4><span>Video / Motion</span></div></div>
  </div>
  <div class="arrows"><span></span><span></span></div>
</section>

<section class="partners">
  <span class="badge"></span><span class="badge"></span><span class="badge"></span><span class="badge"></span><span class="badge"></span>
</section>

<footer class="footer">
  <div class="fcol" style="left:40px;width:150px">
    <h4 class="title">OfficeCore</h4>
    <div class="sub">Responsive business layout</div>
    <p>Approachable IT products and services for business, from procurement to ongoing support.</p>
    <p>Contact us to learn how we can simplify your technology today.</p>
  </div>
  <div class="fcol" style="left:228px;width:140px">
    <h4>LATEST TWEETS</h4>
    <ul><li>Follow us on Chirp</li></ul>
  </div>
  <div class="fcol" style="left:410px;width:170px">
    <h4>LATEST POSTS</h4>
    <ul>
      <li>Free Responsive HTML5 Template</li>
      <li>Design Widget + Free Download</li>
      <li>Free Business Starter Template</li>
      <li>Custom Website Themes</li>
    </ul>
  </div>
  <div class="fcol" style="left:600px;width:140px">
    <h4>SNAPSHOT PHOTOS</h4>
    <div class="photos" role="img" aria-label="Grid of small recent photos"><span></span><span></span><span></span><span></span><span></span><span></span></div>
  </div>
</footer>
<div class="bottom-bar">© Copyright 2013 RTV. All rights reserved.</div>
</body>
</html>
```